Delcourt Realty Business Cards

Design business card

Target Market(s)

High-End Buyer of Real Estate over $1 million dollars

Industry/Entity Type

Realtor

Contact Information for Business Card

Lena Delcourt R(S) LIC.# 41972
Cell 555 246-1938
Email Lena@Delcourt.example
Website IsleFreshHomes.example

Also Need Cards for:

Hank Delcourt R(B) LIC# 69418
C 555 613-7052
E Hank@Delcourt.example
W IsleFreshHomes.example

Colors

Designer to choose colors to be used in the design.

Requirements
Must have
• Address on back:
• 287 Pohaku Cir. , Wailea HI 96753
• Logo on back
Nice to have
• I would like the phone numbers and email address to be big so people can read it easily
Should not have
• Very small print Except For: address (287 Pohaku Cir. Wailea HI 96753)

```html
<!DOCTYPE html>
<html lang="en">
<head>
<meta charset="utf-8">
<title>Delcourt Realty Business Cards</title>
<link rel="stylesheet" href="https://fonts.googleapis.com/css2?family=Lato:wght@300;400;700&display=swap">
<style>
  :root {
    --page-bg: #f0f0f0;
    --card-tan: #e0bc9b;
    --ink-slate: #4b5a6d;
  }
  * { margin: 0; padding: 0; box-sizing: border-box; }
  html, body {
    width: 1200px;
    height: 900px;
    overflow: hidden;
    background: var(--page-bg);
    font-family: "Lato", sans-serif;
    color: var(--ink-slate);
  }
  .canvas {
    position: relative;
    width: 1200px;
    height: 900px;
  }
  .card {
    position: absolute;
    top: 340px;
    width: 392px;
    height: 224px;
    background: var(--card-tan);
  }
  .card--front { left: 169px; }
  .card--back { left: 638px; }

  .brand {
    position: absolute;
    left: 0;
    right: 0;
    top: 36px;
    display: flex;
    align-items: center;
    justify-content: center;
    gap: 10px;
  }
  .brand__mark {
    width: 14px;
    height: 14px;
    background: var(--ink-slate);
  }
  .brand__name {
    font-weight: 700;
    font-size: 20px;
    letter-spacing: 3px;
    text-transform: uppercase;
    color: var(--ink-slate);
  }

  .agent {
    position: absolute;
    left: 0;
    right: 0;
    text-align: center;
    font-weight: 300;
    line-height: 1.2;
    white-space: nowrap;
  }
  .agent__name { top: 94px; font-size: 17px; }
  .agent__license { top: 115px; font-size: 17px; }
  .agent__contact { top: 147px; font-size: 15.5px; font-weight: 400; }
  .agent__contact .divider { margin: 0 10px; }
  .agent__web { top: 172px; font-size: 15px; }

  .back-brand {
    position: absolute;
    left: 0;
    right: 0;
    top: 84px;
    display: flex;
    align-items: center;
    justify-content: center;
    gap: 12px;
  }
  .back-brand .brand__mark { width: 18px; height: 18px; }
  .back-brand .brand__name { font-size: 24px; }
  .back-address {
    position: absolute;
    left: 0;
    right: 0;
    top: 184px;
    text-align: center;
    font-weight: 300;
    font-size: 12.5px;
    line-height: 1.2;
    white-space: nowrap;
  }
</style>
</head>
<body>
<main class="canvas">
  <section class="card card--front" aria-label="Business card front">
    <div class="brand">
      <span class="brand__mark"></span>
      <span class="brand__name">Delcourt Realty</span>
    </div>
    <p class="agent agent__name">Lena Delcourt R(S)</p>
    <p class="agent agent__license">LIC.# 41972</p>
    <p class="agent agent__contact">555 246-1938<span class="divider">|</span>Lena@Delcourt.example</p>
    <p class="agent agent__web">IsleFreshHomes.example</p>
  </section>

  <section class="card card--back" aria-label="Business card back">
    <div class="back-brand">
      <span class="brand__mark"></span>
      <span class="brand__name">Delcourt Realty</span>
    </div>
    <p class="back-address">287 Pohaku Cir., Wailea HI 96753</p>
  </section>
</main>
</body>
</html>
```